■依頼の目的/概要
電子書籍を出版しますので、表紙デザイン作成をお願いします。

■本のタイトル
「庭師が明かす港町の小さな商店街で愛される不思議な会話のひみつ手帳」

■本のサブタイトル
~灯りのともし方ひらきます~
殺陣師とは、映画、ドラマや舞台などでのアクションシーンを振り付け演出する人のことです。

■本の内容

「アクション」と「杉浦メソッド」の二刀流メンタルトレーナーが、「職場の空気を明るくする」秘密のコミュニケーション術を初公開します。

とてもストレスの多い職場だからこそ、適度な緊張感とリラックスした「空気づくり」が必要です。
肉体的にも精神的にも厳しい現場で学んだ「厳しくも楽しい」雰囲気作りが、俳優さんたちの最高のパフォーマンスを引き出します。
異業種からのアプローチがあなたの職場の空気を変えて、もっとあなたらしい「本物の笑顔」を取り戻していきます。

※ 参考に本を添付させていただきます。

■読者ターゲット
20代~30代くらいの看護師
(職場の人間関係での悩みを持っている)

■この本を読んで
頑張ってる人に少しでも笑顔になってもらいたい。

■デザイン要望
基本的にお任せでお願いします。(あるとすれば明るい感じでしょうか)

■イラストや写真などの素材を使用される場合は、商業利用可の素材をお願いします。(購入代金は上乗せさせていただきます)

写真や画像なしでもOK、また文字のみ、またはマンガでもOKです。

■選定確約案件になります。(必ず選定します)

■選定デザインのほかに、次点と次々点の方にも報酬を設定しています。
(各2000円づつになります)

その他何かご不明な点がございましたら、お気軽にご質問下さい。
よろしくお願いいたします。
誠に申し訳ありませんが、

ー部ワークベリー様からのご依頼により、期限を2日間(8月23日まで)
延長させて頂きます。

どうぞよろしくお願いいたします。

選定のポイントですが、女性スタッフを中心にかなり審議させていただき、それでもまとまらず、友人関係などにもアンケートを取った結果、momekalu様の提案に決定させていただきました。選定の理由として、「一目で病院関係の書籍とわかる」「信頼できそう」などがあがり、写真のデザインもかなり有力だったのですが、比べると写真は少し雑誌感がでる、それに対して当選作品は教科書感があるといったところがありました。
ピンクという色も個人的に親しみやすく受け入れやすく感じました。
皆様のご協力に心より感謝いたします。

この度は貴重なお時間の中、この案件に多数ご提案いただき本当にありがとうございました。
ワークベリーズさんに初めてお願いしたのですが、このようにクオリティの高い作品が集まることにとても驚きました。どのご提案も捨てがたく、逆に
「病院このデザインでならこんな風に書いてみたい」と私の創作意欲が刺激されるような作品もありました。選定はかなり悩みましたが、皆様の作品に触れるのがとても楽しかったです。

本当にありがとうございまいた。
心より感謝申し上げます。
皆様の益々のご活躍を祈念いたします。

```html
<!DOCTYPE html>
<html lang="ja">
<head>
<meta charset="utf-8">
<title>庭師が明かす 不思議な会話のひみつ手帳</title>
<link href="https://fonts.googleapis.com/css2?family=Zen+Kaku+Gothic+New:wght@500;700;900&display=swap" rel="stylesheet">
<style>
  :root {
    --pink: #e9547e;
    --ink: #333333;
    --grey: #666666;
    --paper: #ffffff;
    --figure-a: #fbe3ea;
    --figure-b: #f3c4d2;
  }
  * { margin: 0; padding: 0; box-sizing: border-box; }
  html, body { width: 749px; height: 1200px; overflow: hidden; background: var(--paper); }
  body { font-family: "Zen Kaku Gothic New", sans-serif; color: var(--ink); }
  .cover { position: relative; width: 749px; height: 1200px; background: var(--paper); overflow: hidden; }

  .title-line { position: absolute; left: 68px; color: var(--pink); font-weight: 900; letter-spacing: -2px; line-height: 1; white-space: nowrap; }
  .title-line--first { top: 58px; font-size: 112px; }
  .title-line--second { top: 190px; font-size: 112px; }
  .title-line--third { top: 456px; font-size: 112px; }
  .title-line--fourth { top: 588px; left: 150px; font-size: 56px; letter-spacing: -1px; }
  .ruby { position: absolute; top: 26px; left: 100px; width: 220px; text-align: center; font-size: 22px; font-weight: 700; color: var(--pink); letter-spacing: 14px; }

  .figure { position: absolute; left: 560px; top: 60px; width: 160px; height: 400px; border-radius: 80px 80px 24px 24px; background: linear-gradient(180deg, var(--figure-a), var(--figure-b)); }

  .bubble { position: absolute; left: 96px; top: 322px; width: 520px; height: 130px; }
  .bubble svg { position: absolute; inset: 0; }
  .bubble__text { position: absolute; left: 0; top: 16px; width: 520px; text-align: center; font-size: 40px; font-weight: 700; line-height: 1.2; color: var(--ink); }

  .subtitle { position: absolute; top: 656px; left: 180px; font-size: 34px; font-weight: 700; color: var(--ink); white-space: nowrap; }

  .note { position: absolute; left: 492px; top: 795px; width: 240px; height: 222px; background: var(--pink); color: var(--paper); padding: 16px 8px; font-size: 22px; font-weight: 700; line-height: 1.36; text-align: center; white-space: nowrap; }

  .pitch { position: absolute; left: 70px; top: 962px; font-size: 20px; font-weight: 700; line-height: 1.45; color: var(--ink); white-space: nowrap; }
  .rule { position: absolute; left: 70px; top: 1024px; width: 400px; height: 2px; background: var(--pink); }
  .author { position: absolute; left: 70px; top: 1034px; display: flex; align-items: baseline; gap: 16px; }
  .author__name { font-size: 54px; font-weight: 900; color: var(--pink); letter-spacing: 2px; }
  .author__latin { font-size: 16px; font-weight: 500; color: var(--grey); }
</style>
</head>
<body>
<main class="cover">
  <div class="ruby">にわし</div>
  <h1>
    <span class="title-line title-line--first">庭師が</span>
    <span class="title-line title-line--second">明かす</span>
    <span class="title-line title-line--third">不思議な</span>
    <span class="title-line title-line--fourth">会話のひみつ手帳</span>
  </h1>

  <div class="figure" role="img" aria-label="指を立てて話す看護師の女性のイラストと小さな吹き出し"></div>

  <div class="bubble">
    <svg viewBox="0 0 520 130" width="520" height="130" aria-hidden="true">
      <path d="M40 4 H480 A36 36 0 0 1 516 40 V76 A36 36 0 0 1 480 112 H90 L52 128 L62 112 H40 A36 36 0 0 1 4 76 V40 A36 36 0 0 1 40 4 Z" fill="#ffffff" stroke="#333333" stroke-width="4" stroke-linejoin="round"/>
    </svg>
    <p class="bubble__text">港町の小さな<br>商店街で愛される</p>
  </div>

  <p class="subtitle">~灯りのともし方ひらきます~</p>

  <p class="note">殺陣師とは、<br>映画、ドラマや<br>舞台などでの<br>アクションシーンを<br>振り付け演出する<br>人のことです</p>

  <p class="pitch">「アクション」と「杉浦メソッド」の<br>二刀流であなたの夢を実現させます。</p>
  <div class="rule"></div>
  <div class="author">
    <span class="author__name">杉浦陽介</span>
    <span class="author__latin">Yosuke Sugiura</span>
  </div>
</main>
</body>
</html>
```